Brightmoor Partners Branding Revamp

We are a consulting company, looking for a way to display and promote our brand. We have 2 sides to the business- Brightmoor (financial) and Partners (cyber security). The financial side products relate to business necessities: card processing, website design/hosting/maintenance, VoIP phone systems. The cyber security side promotes a bundled package of 4 solutions: network vulnerability scan, dark web scan, anti-ransomeware/malware software, and image-level backups. We want people to understand that partnering with Brightmoor Partners gives them “Elevated Peace of Mind” (tagline). Current badge and logos uploaded.

Target Market(s)

Small businesses

Contact Information for Business Card

Lena Marwick, Vice President, lena@brightmoorpartners.example, 555-806-1937, www.brightmoorpartners.example

Requirements
Nice to have
• I do prefer the darker background for front and back

```html
<!DOCTYPE html>
<html lang="en">
<head>
<meta charset="UTF-8">
<title>Brightmoor Partners – Business Card</title>
<link href="https://fonts.googleapis.com/css2?family=Open+Sans:wght@400;600&display=swap" rel="stylesheet">
<style>
  :root {
    --backdrop: #d4d5d7;
    --card-black: #000000;
    --card-grey: #96979a;
    --brand-red: #e11b22;
    --band-grey-light: #a6a7aa;
    --band-grey-dark: #8c8d90;
    --text-white: #ffffff;
    --text-muted: #b3b4b6;
    --text-dark: #111111;
  }
  html, body {
    margin: 0;
    padding: 0;
    width: 1200px;
    height: 1027px;
    overflow: hidden;
    background: var(--backdrop);
    font-family: "Open Sans", Arial, sans-serif;
  }
  .canvas {
    position: relative;
    width: 1200px;
    height: 1027px;
  }
  .card {
    position: absolute;
    left: 332px;
    width: 535px;
    height: 305px;
    box-shadow: 3px 4px 6px rgba(0,0,0,0.35);
    overflow: hidden;
  }
  .card--front { top: 170px; background: var(--card-black); }
  .card--back  { top: 530px; background: var(--card-grey); }

  .card__shapes {
    position: absolute;
    inset: 0;
    width: 535px;
    height: 305px;
  }

  /* brand lockup */
  .brand {
    position: absolute;
    display: flex;
    flex-direction: column;
    align-items: center;
    font-weight: 600;
    text-transform: uppercase;
  }
  .brand__square {
    width: 46px;
    height: 46px;
    background: var(--brand-red);
    margin-bottom: 16px;
  }
  .brand__name {
    font-size: 19px;
    letter-spacing: 4px;
    line-height: 1;
  }
  .brand__sub {
    font-size: 9px;
    letter-spacing: 2.5px;
    line-height: 1;
    margin-top: 5px;
  }
  .card--front .brand { left: 22px; top: 40px; width: 220px; color: var(--text-white); }
  .card--back  .brand { left: 0; top: 82px; width: 535px; color: var(--text-dark); }
  .card--back  .brand__square { width: 58px; height: 58px; margin-bottom: 18px; }
  .card--back  .brand__name { font-size: 21px; letter-spacing: 5px; }
  .card--back  .brand__sub { font-size: 10px; }

  /* contact block */
  .contact {
    position: absolute;
    right: 38px;
    top: 105px;
    text-align: right;
  }
  .contact__name {
    color: var(--text-white);
    font-size: 22px;
    line-height: 1;
    letter-spacing: 0.5px;
  }
  .contact__title {
    color: var(--text-muted);
    font-size: 15px;
    letter-spacing: 2px;
    margin-top: 10px;
    line-height: 1;
  }
  .contact__details {
    margin-top: 23px;
    color: var(--text-muted);
    font-size: 15px;
    line-height: 21px;
  }

  .website {
    position: absolute;
    left: 36px;
    bottom: 7px;
    color: var(--text-dark);
    font-size: 14px;
    font-weight: 600;
    letter-spacing: 0.6px;
    line-height: 20px;
  }
</style>
</head>
<body>
<main class="canvas">

  <section class="card card--front" aria-label="Business card front">
    <svg class="card__shapes" viewBox="0 0 535 305" aria-hidden="true">
      <defs>
        <linearGradient id="bandGradient" x1="0" y1="0" x2="0" y2="1">
          <stop offset="0" stop-color="var(--band-grey-light)"/>
          <stop offset="1" stop-color="var(--band-grey-dark)"/>
        </linearGradient>
      </defs>
      <polygon class="accent-bar" points="512,42 535,0 535,305 512,305" fill="var(--brand-red)"/>
      <polygon class="website-band" points="0,271 294,271 316,305 0,305" fill="url(#bandGradient)"/>
    </svg>

    <div class="brand">
      <div class="brand__square"></div>
      <div class="brand__name">Brightmoor</div>
      <div class="brand__sub">Partners</div>
    </div>

    <div class="contact">
      <div class="contact__name">Lena Marwick</div>
      <div class="contact__title">Vice President</div>
      <div class="contact__details">
        <div>Mob: 555-806-1937</div>
        <div>lena@brightmoorpartners.example</div>
      </div>
    </div>

    <div class="website">www.brightmoorpartners.example</div>
  </section>

  <section class="card card--back" aria-label="Business card back">
    <div class="brand">
      <div class="brand__square"></div>
      <div class="brand__name">Brightmoor</div>
      <div class="brand__sub">Partners</div>
    </div>
  </section>

</main>
</body>
</html>
```